Business IT Services Billboard to attract local small businesses

We are Brivolane, a premier Managed Service Provider (MSP) specializing in comprehensive IT services and VOIP phone solutions exclusively for businesses. Our goal is to create a dynamic and visually engaging billboard advertisement that not only highlights our cutting-edge IT solutions but also emphasizes our state-of-the-art VOIP phone services. This billboard should communicate our commitment to providing innovative, reliable, and holistic technology solutions.
Target Market(s)
small business
Industry/Entity Type
Information Technology
Colors
Designer to choose colors to be used in the design.
Look and feel
Each slider illustrates characteristics of the customer's brand and the style your logo design should communicate.

```html
<!DOCTYPE html>
<html lang="en">
<head>
<meta charset="utf-8">
<title>Brivolane Billboard</title>
<link rel="stylesheet" href="https://fonts.googleapis.com/css2?family=Ubuntu:wght@300;400;700&display=swap">
<style>
  :root {
    --stage: #e9edf2;
    --board-deep: #0a1f66;
    --board-mid: #0d2a86;
    --board-edge: #1640a8;
    --ice: #d9f6ff;
    --white: #ffffff;
    --sky-blue: #2aa6ff;
    --band: #2f9cf0;
    --band-text: #071a52;
    --globe-core: #2bd0f5;
    --globe-mid: #1a6fe0;
  }
  * { margin: 0; padding: 0; box-sizing: border-box; }
  html, body {
    width: 1200px;
    height: 961px;
    overflow: hidden;
    background: var(--stage);
    font-family: "Ubuntu", sans-serif;
  }
  .canvas {
    position: relative;
    width: 1200px;
    height: 961px;
  }
  .billboard {
    position: absolute;
    left: 40px;
    top: 200px;
    width: 1120px;
    height: 560px;
    overflow: hidden;
    background: linear-gradient(100deg, var(--board-deep) 0%, var(--board-mid) 45%, var(--board-edge) 100%);
    box-shadow: 0 10px 30px rgba(10, 31, 102, 0.25);
  }
  .globe-art {
    position: absolute;
    right: -60px;
    top: -70px;
    width: 640px;
    height: 640px;
    border-radius: 50%;
    background:
      radial-gradient(circle at 40% 30%, var(--globe-core) 0%, var(--globe-mid) 45%, rgba(13, 42, 134, 0) 72%);
  }
  .glow-band {
    position: absolute;
    left: 480px;
    bottom: 0;
    width: 640px;
    height: 240px;
    background: radial-gradient(ellipse at 60% 90%, rgba(42, 166, 255, 0.55) 0%, rgba(42, 166, 255, 0) 70%);
  }
  .brand {
    position: absolute;
    left: 52px;
    top: 48px;
    font-weight: 700;
    font-size: 44px;
    letter-spacing: 2px;
    color: var(--sky-blue);
  }
  .headline {
    position: absolute;
    left: 50px;
    top: 150px;
    width: 720px;
    font-weight: 700;
    font-size: 62px;
    line-height: 1.02;
    color: var(--ice);
  }
  .subline {
    position: absolute;
    left: 52px;
    top: 290px;
    font-weight: 300;
    font-size: 42px;
    color: var(--white);
  }
  .body-copy {
    position: absolute;
    left: 54px;
    top: 392px;
    width: 560px;
    font-weight: 400;
    font-size: 19px;
    line-height: 1.3;
    color: var(--white);
  }
  .cta-band {
    position: absolute;
    left: 0;
    top: 478px;
    padding: 12px 20px 12px 52px;
    background: var(--band);
    font-weight: 400;
    font-size: 21px;
    color: var(--band-text);
  }
</style>
</head>
<body>
  <main class="canvas">
    <section class="billboard">
      <div class="globe-art" role="img" aria-label="Glowing blue globe showing the Americas"></div>
      <div class="glow-band" role="img" aria-label="Arcs of glowing blue light dots rising across the board"></div>
      <div class="brand">BRIVOLANE</div>
      <h1 class="headline">ELEVATE, INTEGRATE &amp;<br>DOMINATE</h1>
      <p class="subline">WITH OUR TECH REVOLUTION</p>
      <p class="body-copy">BRIDGING THE GAP BETWEEN IT EXCELLENCE AND VOIP MASTERY FOR UNRIVALED BUSINESS SUCCESS.</p>
      <p class="cta-band">JOIN THE REVOLUTION AT WWW.BRIVOLANE.COM</p>
    </section>
  </main>
</body>
</html>
```